Wine Label for a White and a Red Wine from Italy

We have a very good idea of what we want with artwork. We need you to please design a 'template' with the text so we can change out the artwork from year to year. Samples are shown of what we are looking for. We are looking for options with the two basic designs. Brand name of wine is: Valora di Castegno. Both wines are in a light green Bordeaux-style bottle (note: we don't show a light green bottle in the mockup but please remember the bottle is light green). Artwork is provided. We'd like to see either the green or blue butterfly on the white wine, the red butterfly is for the red wine. Please base the design on the attached label from Brailey and/or the attached label from Chateau Mervanges.

Target Market(s)

Millennials, women

Requirements
Must have
• The artwork (butterflies) attached.
Nice to have
• Elegant, readable fonts. Please make the text so it can be changed by the printer. Please make it so the artwork can be changed too.

```html
<!DOCTYPE html>
<html lang="en">
<head>
<meta charset="utf-8">
<title>Valora di Castegno – Wine Labels</title>
<link rel="stylesheet" href="https://fonts.googleapis.com/css2?family=Cormorant+Garamond:ital,wght@0,400;0,500;1,500;1,600&display=swap">
<style>
  :root {
    --canvas: #f1f0ef;
    --label: #ffffff;
    --wine-red: #8e2a33;
    --ink: #2b2b2b;
    --muted: #555555;
    --gold-light: #f6d87a;
    --gold: #e9b23c;
    --gold-deep: #d98e2a;
    --red-wing: #b8402a;
    --teal-wing: #1f8d8f;
    --green-wing: #9cb56a;
  }
  * { box-sizing: border-box; margin: 0; padding: 0; }
  html, body {
    width: 1200px; height: 800px; overflow: hidden;
    background: var(--canvas);
  }
  .label-set {
    width: 1200px; height: 800px;
    display: flex; justify-content: center; align-items: center; gap: 60px;
  }
  .label {
    position: relative;
    width: 300px; height: 470px;
    background: var(--label);
    box-shadow: 0 6px 24px rgba(0,0,0,0.10);
    display: flex; flex-direction: column; align-items: center;
    font-family: "Cormorant Garamond", Georgia, serif;
    color: var(--ink);
    text-align: center;
  }
  .gold-band {
    width: 100%; height: 22px; flex: none;
    background: linear-gradient(90deg, var(--gold-deep), var(--gold-light) 30%, var(--gold) 55%, var(--gold-light) 80%, var(--gold-deep));
  }
  .gold-band--top { mask-image: linear-gradient(180deg, #000 55%, transparent); -webkit-mask-image: linear-gradient(180deg, #000 55%, transparent); }
  .gold-band--bottom { margin-top: auto; mask-image: linear-gradient(0deg, #000 55%, transparent); -webkit-mask-image: linear-gradient(0deg, #000 55%, transparent); }
  .brand-name {
    margin-top: 16px;
    font-style: italic; font-weight: 600;
    font-size: 40px; line-height: 1;
    color: var(--wine-red);
  }
  .brand-sub {
    font-style: italic; font-weight: 500;
    font-size: 20px; line-height: 1.1;
    color: var(--wine-red);
  }
  .selection {
    margin-top: 12px;
    font-size: 12px; letter-spacing: 3px; text-transform: uppercase;
    color: var(--muted);
  }
  .artwork {
    margin-top: 14px;
    width: 200px; height: 150px;
    border-radius: 40% 40% 45% 45%;
  }
  .artwork--red { background: radial-gradient(ellipse at center, #e07a45, var(--red-wing) 55%, rgba(184,64,42,0.15) 80%, transparent); }
  .artwork--teal { background: radial-gradient(ellipse at center, #3fb7b3, var(--teal-wing) 50%, rgba(31,141,143,0.15) 78%, transparent); }
  .artwork--green { background: radial-gradient(ellipse at center, #c6d69a, var(--green-wing) 50%, rgba(156,181,106,0.15) 78%, transparent); }
  .vintage {
    margin-top: 14px;
    font-size: 16px; letter-spacing: 4px;
  }
  .varietal {
    font-size: 26px; letter-spacing: 5px; line-height: 1.05;
    font-weight: 500;
  }
  .origin { font-size: 13px; color: var(--muted); }
  .producer {
    margin-top: 10px;
    font-style: italic; font-size: 14px;
    color: var(--wine-red);
  }
  .farming { margin-top: 6px; margin-bottom: 10px; font-size: 13px; }
</style>
</head>
<body>
<main class="label-set">

  <article class="label label--rosso">
    <div class="gold-band gold-band--top"></div>
    <h1 class="brand-name">Valora</h1>
    <p class="brand-sub">di Castegno</p>
    <p class="selection">Barrel Selected</p>
    <div class="artwork artwork--red" role="img" aria-label="Red butterfly artwork"></div>
    <p class="vintage">2018</p>
    <p class="varietal">Roso</p>
    <p class="origin">Piemonte, Italy</p>
    <p class="producer">Artisanally crafted by Cantina Due Colline</p>
    <p class="farming">sustainably farmed</p>
    <div class="gold-band gold-band--bottom"></div>
  </article>

  <article class="label label--bianco">
    <div class="gold-band gold-band--top"></div>
    <h1 class="brand-name">Valora</h1>
    <p class="brand-sub">di Castegno</p>
    <p class="selection">Barrel Selected</p>
    <div class="artwork artwork--teal" role="img" aria-label="Blue-green butterfly artwork"></div>
    <p class="vintage">2018</p>
    <p class="varietal">Bianco</p>
    <p class="origin">Piemonte, Italy</p>
    <p class="producer">Artisanally crafted by Cantina Due Colline</p>
    <p class="farming">sustainably farmed</p>
    <div class="gold-band gold-band--bottom"></div>
  </article>

  <article class="label label--bianco-alt">
    <div class="gold-band gold-band--top"></div>
    <h1 class="brand-name">Valora</h1>
    <p class="brand-sub">di Castegno</p>
    <p class="selection">Barrel Selected</p>
    <div class="artwork artwork--green" role="img" aria-label="Green butterfly artwork"></div>
    <p class="vintage">2018</p>
    <p class="varietal">Bianco</p>
    <p class="origin">Piemonte, Italy</p>
    <p class="producer">Artisanally crafted by Cantina Due Colline</p>
    <p class="farming">sustainably farmed</p>
    <div class="gold-band gold-band--bottom"></div>
  </article>

</main>
</body>
</html>
```